Business Card Design

Electronic Security Installation Specialists

Check out our website at www.brightpulsellc.com to see what we do.

Industry/Entity Type

Business

Contact Information for Business Card

Bright Pulse
Marianne Tolbert
218 Orchard Bend
Shepherdstow, WV 25443

Colors
3176b5
0455a3
ffffff

```html
<!DOCTYPE html>
<html lang="en">
<head>
<meta charset="utf-8">
<title>Bright Pulse — Business Card</title>
<link rel="stylesheet" href="https://fonts.googleapis.com/css2?family=Open+Sans:wght@400;600&display=swap">
<style>
  :root {
    --brand-blue: #0455a3;
    --brand-mid: #3176b5;
    --brand-navy: #1f3f85;
    --card-white: #ffffff;
    --card-silver: #eef0f3;
    --charcoal: #2b2d31;
    --edge-grey: #9aa0a8;
    --page-bg: #d9dadd;
  }
  * { box-sizing: border-box; margin: 0; padding: 0; }
  html, body { width: 1200px; height: 874px; overflow: hidden; }
  body {
    background: var(--page-bg);
    font-family: "Open Sans", Arial, sans-serif;
    display: flex;
    align-items: center;
    justify-content: center;
    gap: 40px;
  }
  .card {
    position: relative;
    width: 540px;
    height: 309px;
    overflow: hidden;
    box-shadow: 0 6px 18px rgba(0,0,0,0.18);
  }

  /* Front */
  .card-front {
    background: linear-gradient(135deg, var(--card-white) 0%, var(--card-silver) 100%);
  }
  .card-front .wave { position: absolute; inset: 0; }
  .brand-mark {
    position: absolute; left: 250px; top: 38px;
    display: flex; align-items: center; gap: 12px;
  }
  .brand-dot {
    width: 28px; height: 28px; border-radius: 50%;
    background: var(--brand-navy);
  }
  .brand-name {
    font-size: 28px; font-weight: 600; letter-spacing: 1px;
    color: var(--brand-blue); text-transform: uppercase;
    white-space: nowrap;
  }
  .person-name {
    position: absolute; left: 252px; top: 98px;
    font-size: 18px; font-weight: 400; letter-spacing: 1px;
    color: var(--brand-blue); text-transform: uppercase;
    white-space: nowrap;
  }
  .accent-square {
    position: absolute; right: 0; top: 100px;
    width: 28px; height: 20px; background: var(--brand-navy);
  }
  .contact {
    position: absolute; left: 252px; top: 150px;
    list-style: none; color: var(--brand-blue);
    font-size: 14px; line-height: 1.45;
  }
  .contact li { display: flex; gap: 10px; align-items: flex-start; margin-bottom: 8px; }
  .contact svg { flex: none; margin-top: 2px; }

  /* Back */
  .card-back {
    background: var(--brand-blue);
    display: flex; flex-direction: column; align-items: center; justify-content: center;
  }
  .back-mark {
    width: 170px; height: 170px; border-radius: 50%;
    background: var(--brand-navy);
    border: 2px solid var(--card-white);
    display: flex; align-items: center; justify-content: center;
  }
  .back-mark span {
    color: var(--card-white); font-size: 22px; font-weight: 600;
  }
  .website {
    margin-top: 22px; color: var(--card-white);
    font-size: 16px; font-weight: 600; letter-spacing: 0.3px;
  }
</style>
</head>
<body>
  <section class="card card-front">
    <svg class="wave" width="540" height="309" viewBox="0 0 540 309" aria-hidden="true">
      <path d="M0 0 H70 C40 90 150 150 150 220 C150 270 110 295 90 309 H0 Z" fill="var(--brand-navy)"/>
      <path d="M70 0 C40 90 150 150 150 220 C150 270 110 295 90 309" fill="none" stroke="var(--charcoal)" stroke-width="8"/>
      <path d="M78 0 C48 90 160 150 160 220 C160 270 120 295 100 309" fill="none" stroke="var(--edge-grey)" stroke-width="2"/>
    </svg>
    <div class="brand-mark">
      <div class="brand-dot"></div>
      <h1 class="brand-name">Bright Pulse</h1>
    </div>
    <p class="person-name">Marianne Tolbert</p>
    <div class="accent-square"></div>
    <ul class="contact">
      <li>
        <svg width="14" height="14" viewBox="0 0 24 24" aria-hidden="true"><path d="M6.6 10.8a15 15 0 0 0 6.6 6.6l2.2-2.2a1 1 0 0 1 1-.25 11.4 11.4 0 0 0 3.6.57 1 1 0 0 1 1 1V20a1 1 0 0 1-1 1A17 17 0 0 1 3 4a1 1 0 0 1 1-1h3.5a1 1 0 0 1 1 1c0 1.25.2 2.45.57 3.570a1 1 0 0 1-.25 1z" fill="var(--charcoal)"/></svg>
        <span>301-555-0182</span>
      </li>
      <li>
        <svg width="14" height="14" viewBox="0 0 24 24" aria-hidden="true"><path d="M12 2a7 7 0 0 0-7 7c0 5.25 7 13 7 13s7-7.75 7-13a7 7 0 0 0-7-7zm0 9.5A2.5 2.5 0 1 1 12 6.5a2.5 2.5 0 0 1 0 5z" fill="var(--charcoal)"/></svg>
        <span>218 Orchard Bend<br>Shepherdstow, WV 25443</span>
      </li>
    </ul>
  </section>

  <section class="card card-back">
    <div class="back-mark"><span>Bright Pulse</span></div>
    <p class="website">www.brightpulsellc.com</p>
  </section>
</body>
</html>
```